BUSINESS CARDS, ENVELOPE, LETTER HEADS AND OTHER STATIONARY
FOR BROOKFERN DATA TECHNOLOGY
I need double sided standard sized Business Card [3.5" x 2"]
Please show me a wide variey of fonts including the ones from the logo
Bright & Fun-filled
Dorian Velmont
Solutions Architect / Technical Sales
82 Pinewhistle Crescent SW
Calgary, Alberta
Canada T2K7M5
dorianv@brookferndataworks.example
http://www.brookferndataworks.example
On the Back of the Bussiness Card I would like to describe a few of the features and solutions that Brookfern Data provides like:
- Electronic Records Management
-IT Solutions (Hardware / Software)
- After hours Technical support (Disaster Recover)
- Procurement
Logo
LOGO file 2
Please Do Not Include the Reflection as part of the logo Thank You

```html
<!DOCTYPE html>
<html lang="en">
<head>
<meta charset="utf-8">
<title>Brookfern Data Technology – Stationery</title>
<link href="https://fonts.googleapis.com/css2?family=Open+Sans:wght@400;600;700&display=swap" rel="stylesheet">
<style>
  :root{
    --bg:#f4f5f6;
    --paper:#ffffff;
    --shadow:rgba(0,0,0,.18);
    --navy:#0c3f7a;
    --blue:#1677c9;
    --sky:#4fb2ea;
    --green:#5fbf3c;
    --ink:#3b3f45;
    --muted:#8a9097;
    --line:#b9bec4;
    --ghost:#e9eef0;
  }
  *{box-sizing:border-box;margin:0;padding:0}
  html,body{width:1200px;height:552px;overflow:hidden;background:var(--bg);
    font-family:"Open Sans",Arial,sans-serif;color:var(--ink)}
  .sheet{position:absolute;background:var(--paper);box-shadow:1px 2px 5px var(--shadow);overflow:hidden}
  .brand{position:absolute;display:flex;align-items:center;gap:5px;
    font-weight:700;color:var(--blue);letter-spacing:.2px;white-space:nowrap}
  .brand-dot{border-radius:50%;background:var(--green);flex:none}
  .contact{position:absolute;font-size:5.5px;line-height:8px;color:var(--muted)}
  .contact span{display:block;white-space:nowrap}
  .watermark{position:absolute;border-radius:50%;
    background:radial-gradient(circle,var(--ghost) 0%,#f3f6f7 70%,transparent 71%)}
  .wave{position:absolute;left:0;bottom:0;width:100%}

  /* letterheads */
  .letterhead{top:19px;width:365px;height:514px}
  .letterhead--fax{left:29px}
  .letterhead--plain{left:408px}
  .letterhead .brand{left:20px;top:20px;font-size:13px}
  .letterhead .brand-dot{width:22px;height:22px}
  .letterhead .contact{left:178px;top:18px}
  .letterhead .watermark{left:85px;top:225px;width:200px;height:200px}
  .fax-title{position:absolute;right:18px;top:71px;font-size:8px;font-weight:700;color:var(--ink)}
  .fax-table{position:absolute;left:20px;top:80px;width:325px;border-collapse:collapse;font-size:6.5px;color:var(--ink)}
  .fax-table td{border:1px solid var(--line);height:14.5px;padding:0 4px}
  .fax-table td.label{width:40px}
  .fax-checks{position:absolute;left:20px;top:163px;display:flex;gap:18px;font-size:6px}
  .fax-checks span{display:flex;align-items:center;gap:4px}
  .fax-checks span::before{content:"";width:6px;height:6px;border:1px solid var(--ink)}

  /* business cards */
  .card{top:26px;width:147px;height:84px}
  .card--front{left:787px;background:linear-gradient(135deg,var(--navy),var(--blue));}
  .card--front .brand-panel{position:absolute;left:0;top:0;width:72px;height:30px;background:var(--paper);border-bottom-right-radius:14px}
  .card--front .brand{left:6px;top:9px;font-size:6.5px;gap:3px}
  .card--front .brand-dot{width:11px;height:11px}
  .card-person{position:absolute;left:10px;top:40px;color:#fff}
  .card-person b{display:block;font-size:7px;font-weight:700}
  .card-person i{display:block;font-style:normal;font-size:4.5px;opacity:.85;margin-top:1px}
  .card--front .contact{left:76px;top:38px;width:66px;color:#dbe8f6;font-size:3.4px;line-height:5.4px}
  .card--back{left:948px}
  .card--back .brand{left:7px;top:20px;font-size:6px;gap:3px}
  .card--back .brand-dot{width:10px;height:10px}
  .services{position:absolute;left:72px;top:17px;list-style:none;font-size:3.5px;line-height:6px;color:var(--muted);white-space:nowrap}

  /* envelopes */
  .envelope{left:787px;width:384px}
  .envelope--a4{top:137px;height:211px}
  .envelope--a4 .brand{left:20px;top:22px;font-size:11px}
  .envelope--a4 .brand-dot{width:18px;height:18px}
  .envelope--a4 .contact{left:20px;top:52px}
  .envelope--a4 .watermark{left:258px;top:30px;width:150px;height:150px}
  .envelope--dl{top:367px;height:166px}
  .envelope--dl .brand{left:50%;transform:translateX(-50%);top:60px;font-size:11px}
  .envelope--dl .brand-dot{width:18px;height:18px}
  .flap-line{position:absolute;left:0;right:0;top:118px;height:1px;background:var(--line)}
</style>
</head>
<body>

<section class="sheet letterhead letterhead--fax">
  <div class="brand"><i class="brand-dot"></i>Brookfern Data</div>
  <div class="contact">
    <span>82 Pinewhistle Crescent SW</span>
    <span>Calgary, Alberta T2K7M5</span>
    <span>dorianv@brookferndataworks.example</span>
    <span>http://www.brookferndataworks.example</span>
  </div>
  <div class="fax-title">FAX</div>
  <table class="fax-table">
    <tr><td class="label">To:</td><td></td><td class="label">From:</td><td></td></tr>
    <tr><td class="label">Fax:</td><td></td><td class="label">Pages:</td><td></td></tr>
    <tr><td class="label">Phone:</td><td></td><td class="label">Date:</td><td></td></tr>
    <tr><td class="label">Re:</td><td></td><td class="label">CC:</td><td></td></tr>
  </table>
  <div class="fax-checks">
    <span>Urgent</span><span>For Review</span><span>Please Comment</span><span>Please Reply</span><span>Please Recycle</span>
  </div>
  <div class="watermark" role="img" aria-label="Faint background circle"></div>
  <svg class="wave" viewBox="0 0 365 40" preserveAspectRatio="none" aria-hidden="true">
    <path d="M0 22 Q180 8 365 20 L365 40 L0 40Z" fill="var(--green)"/>
    <path d="M0 27 Q180 14 365 25 L365 40 L0 40Z" fill="var(--blue)"/>
  </svg>
</section>

<section class="sheet letterhead letterhead--plain">
  <div class="brand"><i class="brand-dot"></i>Brookfern Data</div>
  <div class="contact">
    <span>82 Pinewhistle Crescent SW</span>
    <span>Calgary, Alberta T2K7M5</span>
    <span>dorianv@brookferndataworks.example</span>
    <span>http://www.brookferndataworks.example</span>
  </div>
  <div class="watermark" role="img" aria-label="Faint background circle"></div>
  <svg class="wave" viewBox="0 0 365 40" preserveAspectRatio="none" aria-hidden="true">
    <path d="M0 22 Q180 8 365 20 L365 40 L0 40Z" fill="var(--green)"/>
    <path d="M0 27 Q180 14 365 25 L365 40 L0 40Z" fill="var(--blue)"/>
  </svg>
</section>

<section class="sheet card card--front">
  <div class="brand-panel"></div>
  <div class="brand"><i class="brand-dot"></i>Brookfern Data</div>
  <div class="card-person"><b>Dorian Velmont</b><i>Solutions Architect</i></div>
  <div class="contact">
    <span>82 Pinewhistle Crescent SW</span>
    <span>Calgary, Alberta T2K7M5</span>
    <span>dorianv@brookferndataworks.example</span>
  </div>
</section>

<section class="sheet card card--back">
  <div class="brand"><i class="brand-dot"></i>Brookfern Data</div>
  <ul class="services">
    <li>Electronic Records Management</li>
    <li>IT Solutions (Hardware / Software)</li>
    <li>After Hours Technical Support</li>
    <li>Procurement</li>
  </ul>
  <svg class="wave" viewBox="0 0 147 12" preserveAspectRatio="none" aria-hidden="true">
    <path d="M0 6 Q70 1 147 5 L147 12 L0 12Z" fill="var(--green)"/>
    <path d="M0 8 Q70 3 147 7 L147 12 L0 12Z" fill="var(--blue)"/>
  </svg>
</section>

<section class="sheet envelope envelope--a4">
  <div class="brand"><i class="brand-dot"></i>Brookfern Data</div>
  <div class="contact">
    <span>82 Pinewhistle Crescent SW</span>
    <span>Calgary, Alberta T2K7M5</span>
    <span>dorianv@brookferndataworks.example</span>
    <span>http://www.brookferndataworks.example</span>
  </div>
  <div class="watermark" role="img" aria-label="Faint background circle"></div>
  <svg class="wave" viewBox="0 0 384 30" preserveAspectRatio="none" aria-hidden="true">
    <path d="M0 16 Q190 4 384 14 L384 30 L0 30Z" fill="var(--green)"/>
    <path d="M0 20 Q190 9 384 18 L384 30 L0 30Z" fill="var(--blue)"/>
  </svg>
</section>

<section class="sheet envelope envelope--dl">
  <div class="brand"><i class="brand-dot"></i>Brookfern Data</div>
  <div class="flap-line"></div>
  <svg class="wave" viewBox="0 0 384 20" preserveAspectRatio="none" aria-hidden="true">
    <path d="M0 12 Q190 4 384 10 L384 20 L0 20Z" fill="var(--sky)"/>
    <path d="M0 15 Q190 8 384 13 L384 20 L0 20Z" fill="var(--blue)"/>
  </svg>
</section>

</body>
</html>
```